Website - Tides Of Motion

We are catalysts of change in people's lives.
We work with individuals and professionals to bring about instant substantial & transforming change in their lives.
We provide one-on-one lifestyle coaching by an experienced practitioner.
Our existing website is www.tidesofmotion.biz & this site contains our the basis for the content of our desired new project, so please examine this carefully.
We require a professional and captivating website that will instantly impress, engage invite our readers to click & invest their lives.
Our services do not come cheap, but are second to none.
Our website must be contemporary whilst reflecting indisputable class & ultra-confidence in the success of our work.
Target Market(s)
Those who seek to want to change in their lives. Those aged primarily between 30 and 50 years of age, male or female.
Industry/Entity Type
Work

```html
<!DOCTYPE html>
<html lang="en">
<head>
<meta charset="utf-8">
<title>Tides Of Motion</title>
<link rel="stylesheet" href="https://fonts.googleapis.com/css2?family=Open+Sans:wght@300;400;600&family=PT+Sans+Narrow&family=Oxygen:wght@300;400&display=swap">
<style>
:root{
  --page:#000;
  --ink:#e6e6e6;
  --muted:#bdbdbd;
  --card:#232323;
  --card-line:#3c3c3c;
  --orange-top:#f9a825;
  --orange-bottom:#ee860c;
  --nav-divider:#d97708;
  --green:#7cbf2f;
  --green-dark:#5e9a1c;
  --cyan:#3ec3dc;
  --cyan-dark:#1fa2bd;
  --footer:#2b2b2b;
  --footer-link:#d8d8d8;
  --footer-note:#6b6b6b;
  --hero-fill:#5a7a1e;
  --photo-business:#4a4a4c;
  --photo-individual:#8a7444;
  --photo-lifestyle:#8e8a6a;
}
*{margin:0;padding:0;box-sizing:border-box}
html,body{width:1071px;height:1200px;overflow:hidden;background:var(--page)}
body{position:relative;font-family:"Open Sans",sans-serif;color:var(--ink)}

.brand{position:absolute;left:92px;top:44px;display:flex;align-items:center;gap:14px}
.brand-mark{width:40px;height:40px;border-radius:50%;background:var(--orange-bottom)}
.brand-name{font-family:"PT Sans Narrow",sans-serif;font-size:34px;color:#d9d9d9;line-height:1}

.social-top{position:absolute;left:892px;top:90px;display:flex;gap:8px}
.social-top span{width:20px;height:20px;background:#4a4a4a;border-radius:2px}

.main-nav{position:absolute;left:77px;top:128px;width:918px;height:47px;
  background:linear-gradient(var(--orange-top),var(--orange-bottom));display:flex}
.main-nav a{font-family:"PT Sans Narrow",sans-serif;font-size:16px;color:#fff;text-decoration:none;
  display:flex;align-items:center;justify-content:center;border-right:1px solid var(--nav-divider)}

.hero{position:absolute;left:77px;top:175px;width:918px;height:351px;overflow:hidden;background:var(--hero-fill)}
.hero-title{position:absolute;left:57px;top:195px;font-family:"Oxygen",sans-serif;font-weight:300;font-size:36px;color:#fff;line-height:1}
.hero-sub{position:absolute;left:57px;top:242px;font-family:"Oxygen",sans-serif;font-weight:300;font-size:23px;color:#fff;line-height:1}
.hero-dots{position:absolute;left:418px;top:326px}

.service{position:absolute;top:548px;width:297px;height:269px;background:var(--card);border:1px solid var(--card-line)}
.service-photo{height:122px;border-bottom:1px solid var(--card-line)}
.service h2{font-weight:400;font-size:21px;line-height:26px;margin:14px 0 0 18px;color:#f0f0f0}
.service p{font-size:11px;line-height:18px;color:var(--muted);margin:6px 0 0 18px;white-space:nowrap}
.btn{position:absolute;left:18px;top:227px;height:23px;padding:0 14px;border-radius:3px;
  font-size:11px;line-height:23px;color:#3a2a10;text-decoration:none}
.btn-orange{background:linear-gradient(var(--orange-top),var(--orange-bottom))}
.btn-green{background:linear-gradient(var(--green),var(--green-dark));color:#1d3306}
.btn-cyan{background:linear-gradient(var(--cyan),var(--cyan-dark));color:#0b3340}

.divider{position:absolute;left:75px;top:845px;width:920px;height:1px;background:#333}

.welcome{position:absolute;left:80px;top:876px;width:580px}
.welcome h1{font-weight:400;font-size:24px;color:#eee}
.welcome p{font-size:11px;line-height:20px;color:#dcdcdc;margin-top:12px}

.changes{position:absolute;left:711px;top:874px;width:280px}
.changes h2{font-weight:400;font-size:22px;color:#eee}
.changes ul{list-style:none;margin-top:12px}
.changes li{display:flex;gap:12px;font-size:11px;line-height:16px;color:#bdbdbd;margin-bottom:9px}
.changes svg{flex:none;margin-top:1px}

.site-footer{position:absolute;left:0;top:1093px;width:1071px;height:107px;background:var(--footer)}
.footer-nav{position:absolute;left:75px;top:30px;font-size:12.5px;color:var(--footer-link)}
.footer-nav a{color:var(--footer-link);text-decoration:none}
.footer-nav .sep{margin:0 8px;color:#888}
.copyright{position:absolute;left:75px;top:62px;font-size:11px;font-weight:300;color:var(--footer-note)}
.social-foot{position:absolute;left:865px;top:27px;display:flex;gap:3px}
.social-foot span{width:27px;height:27px;border-radius:50%;background:#d6d6d6}
</style>
</head>
<body>

<header>
  <div class="brand">
    <span class="brand-mark"></span>
    <span class="brand-name">Tides Of Motion</span>
  </div>
  <div class="social-top"><span></span><span></span><span></span><span></span></div>
  <nav class="main-nav">
    <a href="#" style="width:100px">HOME</a>
    <a href="#" style="width:118px">ABOUT US</a>
    <a href="#" style="width:109px">BUSINESS</a>
    <a href="#" style="width:150px">PROFESSIONAL</a>
    <a href="#" style="width:126px">INDIVIDUAL</a>
    <a href="#" style="width:105px">CONTACT</a>
  </nav>
</header>

<section class="hero" role="img" aria-label="Photo of sunlight shining through a green forest">
  <div class="hero-title">Force to Change in your Life</div>
  <div class="hero-sub">Duis tincidunt lectus quis dui</div>
  <svg class="hero-dots" width="82" height="25" viewBox="0 0 82 25">
    <path d="M0 25 Q8 25 12 12 Q16 0 28 0 H54 Q66 0 70 12 Q74 25 82 25 Z" fill="rgba(40,40,20,.7)"/>
    <circle cx="23" cy="14" r="4.5" fill="#ddd"/><circle cx="35" cy="14" r="4.5" fill="#ddd"/>
    <circle cx="47" cy="14" r="4.5" fill="#ddd"/><circle cx="59" cy="14" r="4.5" fill="#ddd"/>
  </svg>
</section>

<article class="service" style="left:75px">
  <div class="service-photo" role="img" aria-label="Portrait photo of a businessman" style="background:var(--photo-business)"></div>
  <h2>Business</h2>
  <p>Duis tincidunt lectus quis dui viverra vestibulum.<br>Suspendisse vulputate aliquam dui. Nulla elemen-<br>tum dui ut augue Aliquam vehicula mi</p>
  <a class="btn btn-orange" href="#">Read More</a>
</article>

<article class="service" style="left:387px">
  <div class="service-photo" role="img" aria-label="Photo of a kayaker on a misty lake" style="background:var(--photo-individual)"></div>
  <h2>Individual</h2>
  <p>Duis tincidunt lectus quis dui viverra vestibulum.<br>Suspendisse vulputate aliquam dui. Nulla elemen-<br>tum dui ut augue. Aliquam vehicula</p>
  <a class="btn btn-green" href="#">Read More</a>
</article>

<article class="service" style="left:699px">
  <div class="service-photo" role="img" aria-label="Photo of a woman with open arms in a field" style="background:var(--photo-lifestyle)"></div>
  <h2>Lifestyle Coaching</h2>
  <p>Duis tincidunt lectus quis dui viverra vestibulum.<br>Suspendisse vulputate aliquam dui. Nulla elemen-<br>tum dui ut augue. Aliquam vehicula mi at mauris</p>
  <a class="btn btn-cyan" href="#">Read More</a>
</article>

<div class="divider"></div>

<section class="welcome">
  <h1>Welcome to Our Website Mainpage..</h1>
  <p>Our clients experience their desired instant &amp; permanent transformation, emerging from our consultations ready to take on their world from a vastly different paradigm At Tides Of Motion, our Master Practitioner will inspire you, shifting your perspective &amp; facilitating your mind with the freedom to realise your dreams</p>
  <p>Join Marcus Hale, Elena Voss, R.J. Penrose, Tomas Reed, Nina Carrow, Della Frost and hundreds of thousands of others who are achieving the life changing, consistent results you are dreaming of now.</p>
</section>

<aside class="changes">
  <h2>Changes is Yours</h2>
  <ul>
    <li><svg width="18" height="18" viewBox="0 0 18 18"><circle cx="9" cy="9" r="9" fill="#9a9a9a"/><path d="M5 9.5l2.7 2.6L13 6.5" stroke="#222" stroke-width="2" fill="none"/></svg>More choices about your behaviours and emotions</li>
    <li><svg width="18" height="18" viewBox="0 0 18 18"><circle cx="9" cy="9" r="9" fill="#9a9a9a"/><path d="M5 9.5l2.7 2.6L13 6.5" stroke="#222" stroke-width="2" fill="none"/></svg>Improve your relationships and the ways you communicate</li>
    <li><svg width="18" height="18" viewBox="0 0 18 18"><circle cx="9" cy="9" r="9" fill="#9a9a9a"/><path d="M5 9.5l2.7 2.6L13 6.5" stroke="#222" stroke-width="2" fill="none"/></svg>Create better results through becoming a greater thinker</li>
  </ul>
</aside>

<footer class="site-footer">
  <nav class="footer-nav">
    <a href="#">HOME</a><span class="sep">|</span><a href="#">ABOUT US</a><span class="sep">|</span><a href="#">BUSINESS</a><span class="sep">|</span><a href="#">PROFESSIONAL</a><span class="sep">|</span><a href="#">INDIVIDUAL</a><span class="sep">|</span><a href="#">CONTACT</a>
  </nav>
  <div class="copyright">© 2013 Company Name. All right resered</div>
  <div class="social-foot"><span></span><span></span><span></span><span></span></div>
</footer>

</body>
</html>
```